Computer consultant business card

Brimlo Software is a newly started computer consulting company. It's a small one-man company that provides mostly Velunix applications but also websites in collaboration with designers. I'm running this company on the side of full time university studies.

I want the final design to be clean and memorable. Be creative! :)

Some inspiration:
http://www.tavelpix.net/design/73519
http://www.tavelpix.net/design/2739566/business-card-design-by-quillbop
http://www.tavelpix.net/design/804613/business-card-design-by-lorvena-brukwaldsen

See attachment for my company logo.
Updates

I would like to thank everyone for submitting! I'll need a couple of days to review and ultimately select a design.

Target Market(s)

Non-technical entrepreneurs and small companies.

Industry/Entity Type

University

Requirements
Must have
• My company logo.
In any way, both colors from my logo.
First- and last name, e-mail and phone number.
Double-sided design.
Nice to have
• Something creative with the symbol in my logo

```html
<!DOCTYPE html>
<html lang="en">
<head>
<meta charset="utf-8">
<title>Brimlo Software – Business Card</title>
<link rel="stylesheet" href="https://fonts.googleapis.com/css2?family=Quicksand:wght@400;500;600&display=swap">
<style>
  :root {
    --page-bg: #e9ecef;
    --card-white: #ffffff;
    --ink-dark: #3a3a3c;
    --brand-blue: #1f7ae0;
    --pattern-light: #45b0ec;
    --pattern-deep: #2a86de;
    --card-shadow: 0 6px 22px rgba(30, 40, 60, 0.18);
  }
  * { box-sizing: border-box; margin: 0; padding: 0; }
  html, body {
    width: 1200px;
    height: 960px;
    overflow: hidden;
    background: var(--page-bg);
    font-family: "Quicksand", sans-serif;
  }
  .sheet {
    position: relative;
    width: 1200px;
    height: 960px;
  }
  .card {
    position: absolute;
    left: 250px;
    width: 700px;
    height: 400px;
    box-shadow: var(--card-shadow);
  }
  .card--front {
    top: 50px;
    background: var(--card-white);
  }
  .card--back {
    top: 500px;
    background: linear-gradient(135deg, var(--pattern-light) 0%, var(--pattern-deep) 100%);
  }
  .brand {
    position: absolute;
    left: 52px;
    top: 60px;
    display: flex;
    align-items: center;
    gap: 18px;
  }
  .brand__dot {
    width: 62px;
    height: 62px;
    border-radius: 50%;
    background: var(--brand-blue);
  }
  .brand__name {
    font-size: 64px;
    font-weight: 600;
    color: var(--ink-dark);
    letter-spacing: 1px;
    line-height: 1;
  }
  .holder-name {
    position: absolute;
    left: 80px;
    bottom: 78px;
    font-size: 30px;
    font-weight: 500;
    color: var(--ink-dark);
    letter-spacing: 1.5px;
  }
  .contact {
    position: absolute;
    left: 430px;
    bottom: 96px;
    list-style: none;
    font-size: 16px;
    font-weight: 500;
    color: var(--ink-dark);
    line-height: 1.3;
  }
  .contact__label {
    color: var(--brand-blue);
    display: inline-block;
    width: 14px;
  }
</style>
</head>
<body>
  <main class="sheet">
    <section class="card card--front" aria-label="Business card front">
      <div class="brand">
        <span class="brand__dot" aria-hidden="true"></span>
        <span class="brand__name">brimlo</span>
      </div>
      <p class="holder-name">MAREN HOLT</p>
      <ul class="contact">
        <li><span class="contact__label">t</span> 555.014.2273</li>
        <li><span class="contact__label">e</span> maren_holt@brimlo.net</li>
      </ul>
    </section>
    <section class="card card--back" role="img" aria-label="Card back: repeating pattern of the brand symbol in dark grey and blue tones"></section>
  </main>
</body>
</html>
```